Graphics for New Online Software

Looking at a designer to design a UI/UX Interface for an Online Events Platform (just JPEG) and some corresponding images for a website content (i.e. features etc)

Deliverables:
1x User Interface Design for the Platform (refer to attachment)
5-6x Feature Listing Images (refer to attachment)

Target Market(s)

Technology, Online Users Etc

Industry/Entity Type

Software Developer

Number of Pages Required

1 page

Font styles to use
Sans Serif

Colors
34a7d8
0493ce
3176b5
85acd3

Requirements
Must have
• Looks like a well built software - examples:
https://velmora.io/
https://quillard.com/

All the images should look very professional, as though you are using it on the online platform itself.
Nice to have
• Refer to attached "Feature Listing" and Logo

```html
<!DOCTYPE html>
<html lang="en">
<head>
<meta charset="utf-8">
<title>Eventrix – Online Events Platform UI</title>
<link href="https://fonts.googleapis.com/css2?family=Roboto:wght@400;500;700;900&display=swap" rel="stylesheet">
<style>
:root{
  --board:#cfd0d2;
  --panel:#f4f4f4;
  --white:#ffffff;
  --ink:#1d1d1f;
  --muted:#555a60;
  --nav:#2a62a8;
  --nav-active:#1683c9;
  --nav-line:#2458a0;
  --accent:#0493ce;
  --accent-dark:#3176b5;
  --accent-soft:#85acd3;
  --line:#dcdfe3;
}
*{box-sizing:border-box;margin:0;padding:0}
html,body{width:1147px;height:1200px;overflow:hidden}
body{background:var(--board);font-family:"Roboto",Arial,sans-serif;color:var(--ink);position:relative}
.screen{position:absolute;width:535px;background:var(--panel);display:grid;grid-template-rows:33px 1fr;grid-template-columns:73px 1fr;box-shadow:0 1px 3px rgba(0,0,0,.08)}
.topbar{grid-column:1/3;background:var(--white);display:flex;align-items:center;justify-content:space-between;padding:0 12px 0 7px;border-bottom:1px solid #eceef0}
.brand{display:flex;align-items:center;gap:4px;font-size:14px;font-weight:900;color:var(--ink);letter-spacing:-.2px}
.brand-mark{width:9px;height:9px;background:var(--accent-dark)}
.duration{display:flex;align-items:center;gap:6px}
.duration-label{font-size:5px;font-weight:700;text-align:right;line-height:1.25}
.duration-sep{width:1px;height:17px;background:#cfd2d6}
.clock{font-size:9px;font-weight:700;line-height:1;text-align:center}
.clock small{display:block;font-size:4px;font-weight:500;word-spacing:3px;margin-top:1px}
.sidenav{background:var(--nav);display:flex;flex-direction:column}
.nav-item{height:52px;padding:14px 0 0 12px;color:var(--white);font-size:6px;font-weight:700;letter-spacing:.3px;border-bottom:1px solid var(--nav-line);line-height:1.55}
.nav-item.tall{height:58px}
.nav-item.active{background:var(--nav-active)}
.nav-item svg{display:block;width:13px;height:13px;margin-bottom:5px;fill:none;stroke:var(--white);stroke-width:1.1}
.main{position:relative}
.card{position:absolute;background:var(--white);box-shadow:0 0 2px rgba(0,0,0,.06)}
.card-title{font-size:7.5px;font-weight:500;letter-spacing:.2px}
.agenda{display:flex;align-items:center;gap:12px;padding:0 12px}
.agenda-icon{width:25px;height:25px;border-radius:50%;background:var(--accent);flex:none;display:flex;align-items:center;justify-content:center}
.agenda-icon svg{width:12px;height:12px;fill:none;stroke:#fff;stroke-width:1.4}
.agenda p{font-size:5px;color:var(--muted);line-height:1.55;margin-top:3px;max-width:320px}
.program{padding:10px 10px}
.program-grid{display:grid;grid-template-columns:repeat(4,1fr);gap:6px;margin-top:8px}
.program-item{border:1px solid var(--line);padding:9px 8px;height:70px}
.program-item h4{font-size:4.8px;font-weight:500;line-height:1.6}
.program-item p{font-size:4.6px;color:var(--muted);line-height:1.35;margin-top:5px}
.speakers{padding:10px 10px}
.speaker-grid{display:grid;grid-template-columns:repeat(5,1fr);gap:3.5px;margin-top:6px}
.speaker{border:1px solid var(--line)}
.speaker-photo{height:83px}
.speaker-name{height:17px;font-size:4.8px;font-weight:500;padding:6px 0 0 6px;white-space:nowrap}
.copyright{position:absolute;left:0;right:0;text-align:center;font-size:4.3px;color:#333}
.video{position:absolute;left:10px;top:12px;width:321px;height:252px;background:linear-gradient(135deg,#6e5a45 0%,#8b7a66 35%,#4d6b88 70%,#2c3e52 100%)}
.play{position:absolute;left:144px;top:112px;width:32px;height:22px;border-radius:6px;background:var(--accent);display:flex;align-items:center;justify-content:center}
.play svg{width:9px;height:9px;fill:#fff}
.video-caption{position:absolute;left:9px;bottom:8px;color:#fff;font-size:7px;font-weight:700;letter-spacing:.2px}
.chat{position:absolute;left:343px;top:0;width:119px;height:264px;background:var(--white);padding:12px 9px 0 10px}
.chat h3{font-size:6.5px;font-weight:700}
.chat-list{margin-top:8px;display:flex;flex-direction:column;gap:12.5px}
.msg{display:grid;grid-template-columns:17px 1fr auto;gap:5px;align-items:start}
.avatar{width:17px;height:17px;border-radius:50%;background:linear-gradient(160deg,#b7967c,#5c4a3f)}
.msg b{display:block;font-size:5px;font-weight:500;color:var(--accent-dark)}
.msg span{display:block;font-size:4.2px;color:#333;line-height:1.25;margin-top:2px}
.msg time{font-size:4px;color:#333}
.chat-input{position:absolute;left:0;right:0;bottom:0;height:22px;border-top:1px solid var(--line);display:flex;align-items:center;justify-content:space-between;padding:0 10px 0 9px;font-size:4.6px;font-style:italic;color:#333}
.chat-input svg{width:7px;height:7px;fill:#333}
.rooms{position:absolute;left:17px;top:17px;display:grid;grid-template-columns:209px 209px;grid-auto-rows:117px;gap:6px}
.room{position:relative;background:linear-gradient(160deg,#5c5b5a,#2e2d2c 60%,#3e3a36);color:#fff;text-align:center}
.room h3{margin-top:40px;font-size:9.5px;font-weight:500;letter-spacing:.4px}
.room-time{display:inline-block;margin-top:6px;background:var(--nav-active);font-size:9.5px;font-weight:500;padding:3px 8px}
.room-count{position:absolute;right:7px;bottom:6px;font-size:7.5px;font-weight:700}
.zoom{position:absolute;right:6px;top:7px;width:12px;height:12px;border-radius:50%;background:#fff;display:flex;align-items:center;justify-content:center}
.zoom svg{width:6px;height:6px;fill:none;stroke:#222;stroke-width:2}
.expo{position:absolute;left:50px;top:21px;width:354px;height:214px;background:radial-gradient(ellipse at center,#e9dfd6 0%,#f1ece7 55%,#f4f4f4 80%)}
.expo-actions{position:absolute;top:258px;left:173px;display:flex;gap:6px}
.btn{background:var(--nav-active);color:#fff;font-size:6px;font-weight:700;padding:6px 8px;letter-spacing:.3px}
.badge{position:absolute;top:21px;height:57px;background:var(--white);text-align:center;box-shadow:0 0 2px rgba(0,0,0,.06)}
.badge svg.ic{display:block;margin:13px auto 0;width:14px;height:14px;fill:none;stroke:var(--accent);stroke-width:1.5}
.badge p{font-size:6px;font-weight:500;margin-top:6px;letter-spacing:.2px}
.badge .tick{position:absolute;right:6px;top:6px;width:7px;height:7px;fill:none;stroke:var(--accent-dark);stroke-width:2.2}
.points{position:absolute;left:192px;top:110px;width:70px;height:70px;border-radius:50%;border:1.5px solid #d5d7da;background:var(--white);text-align:center}
.points strong{display:block;font-size:24px;font-weight:700;color:var(--accent-dark);margin-top:10px;line-height:1}
.points span{display:block;font-size:7px;font-weight:500;margin-top:4px}
.reward-title{position:absolute;left:0;right:0;top:199px;text-align:center;font-size:10.5px;font-weight:500;letter-spacing:.1px}
.reward-note{position:absolute;left:0;right:0;top:220px;text-align:center;font-size:6px;color:#222}
.reward-link{position:absolute;left:159px;top:245px;width:146px;height:15px;border:1px solid #aab0b6;background:var(--white);font-size:6px;text-align:center;line-height:13px}
.reward-link a{color:var(--accent-dark);text-decoration:none}
</style>
</head>
<body>
<svg width="0" height="0" style="position:absolute" aria-hidden="true">
  <symbol id="i-cal" viewBox="0 0 12 12"><rect x="1" y="2" width="10" height="9" rx="1"/><path d="M1 4.5h10M4 1v2M8 1v2M3 6.5h1M5.5 6.5h1M8 6.5h1M3 8.7h1M5.5 8.7h1M8 8.7h1"/></symbol>
  <symbol id="i-stage" viewBox="0 0 12 12"><path d="M1 11h10M2 11V8h2v3M5 11V6h2v5M8 11V4h2v7M1.5 5.5l3-2.5 2 1.5 4-3"/></symbol>
  <symbol id="i-break" viewBox="0 0 12 12"><circle cx="6" cy="6" r="3.6"/><path d="M6 .8v1.6M6 9.6v1.6M.8 6h1.6M9.6 6h1.6M2.3 2.3l1.1 1.1M8.6 8.6l1.1 1.1M9.7 2.3 8.6 3.4M3.4 8.6 2.3 9.7M4.4 6l1.1 1.1 2-2.2"/></symbol>
  <symbol id="i-expo" viewBox="0 0 12 12"><circle cx="6" cy="2" r="1.3"/><path d="M4.5 4.2h3v3.5h-3zM5.3 7.7v2.3M6.7 7.7v2.3M1.5 9.5c0 1 2 1.8 4.5 1.8s4.5-.8 4.5-1.8"/></symbol>
  <symbol id="i-reward" viewBox="0 0 12 12"><circle cx="6" cy="4.6" r="3.6"/><path d="m6 2.7.6 1.3 1.4.1-1 1 .3 1.4L6 5.8l-1.3.7.3-1.4-1-1 1.4-.1zM3.8 7.6 2.8 11l1.7-.8 1 1.1M8.2 7.6l1 3.4-1.7-.8-1 1.1"/></symbol>
  <symbol id="i-check" viewBox="0 0 12 12"><path d="M1.5 6.5 4.5 9.5 10.5 2.5"/></symbol>
  <symbol id="i-hands" viewBox="0 0 14 12"><path d="M1 4l3-1.5 3 1.5 3-1.5 3 1.5M4 2.5 1 7l3 2.5 2 1.5 2-1.5 2-2M10 2.5 13 7l-3 2.5M5 5.5l2 2"/></symbol>
  <symbol id="i-search" viewBox="0 0 10 10"><circle cx="4" cy="4" r="2.8"/><path d="M6 6l3 3"/></symbol>
  <symbol id="i-agenda" viewBox="0 0 12 12"><rect x="1.5" y="2" width="9" height="9" rx="1"/><path d="M4 1v2M8 1v2M3.8 6.8 5.4 8.4 8.3 5.2"/></symbol>
</svg>

<!-- Event info screen -->
<section class="screen" style="left:24px;top:29px;height:411px">
  <header class="topbar">
    <div class="brand"><span>EVENTRIX</span><span class="brand-mark"></span></div>
    <div class="duration"><div class="duration-label">EVENT<br>DURATION</div><div class="duration-sep"></div><div class="clock">16:55<small>HH MM</small></div></div>
  </header>
  <nav class="sidenav">
    <div class="nav-item active"><svg><use href="#i-cal"/></svg>EVENT INFO</div>
    <div class="nav-item"><svg><use href="#i-stage"/></svg>STAGE</div>
    <div class="nav-item"><svg><use href="#i-break"/></svg>BREAKOUTS</div>
    <div class="nav-item tall"><svg><use href="#i-expo"/></svg>VIRTUAL<br>EXHIBITION</div>
    <div class="nav-item"><svg><use href="#i-reward"/></svg>REWARDS</div>
  </nav>
  <main class="main">
    <div class="card agenda" style="left:13px;top:15px;width:436px;height:56px">
      <div class="agenda-icon"><svg><use href="#i-agenda"/></svg></div>
      <div><div class="card-title">AGENDA</div><p>Lorem ipsum dolor sit amet, consectetur adipiscing elit, sed do eiusmod tempor incididunt ut labore et dolore magna aliqua. Ut enim ad minim veniam, quis nostrud exercitation ullamco laboris nisi ut aliquip.</p></div>
    </div>
    <div class="card program" style="left:13px;top:81px;width:436px;height:107px">
      <div class="card-title">PROGRAMMING</div>
      <div class="program-grid">
        <div class="program-item"><h4>LOREM IPSUM DOLOR SIT AMET CONSECTETUR ADIPISCING</h4><p>Lorem ipsum dolor sit amet, consectetur adipiscing elit, sed do eiusmod tempor elit, sed do eiusmod tempor incididunt</p></div>
        <div class="program-item"><h4>LOREM IPSUM DOLOR SIT AMET CONSECTETUR ADIPISCING</h4><p>Lorem ipsum dolor sit amet, consectetur adipiscing elit, sed do eiusmod tempor elit, sed do eiusmod tempor incididunt</p></div>
        <div class="program-item"><h4>LOREM IPSUM DOLOR SIT AMET CONSECTETUR ADIPISCING</h4><p>Lorem ipsum dolor sit amet, consectetur adipiscing elit, sed do eiusmod tempor elit, sed do eiusmod tempor incididunt</p></div>
        <div class="program-item"><h4>LOREM IPSUM DOLOR SIT AMET CONSECTETUR ADIPISCING</h4><p>Lorem ipsum dolor sit amet, consectetur adipiscing elit, sed do eiusmod tempor elit, sed do eiusmod tempor incididunt</p></div>
      </div>
    </div>
    <div class="card speakers" style="left:13px;top:201px;width:436px;height:137px">
      <div class="card-title">SPEAKERS</div>
      <div class="speaker-grid">
        <div class="speaker"><div class="speaker-photo" role="img" aria-label="Portrait photo of a speaker in a light blue shirt" style="background:linear-gradient(160deg,#8a7a6a,#4f6b8c)"></div><div class="speaker-name">TALIA BRENNER</div></div>
        <div class="speaker"><div class="speaker-photo" role="img" aria-label="Portrait photo of a speaker in a grey suit" style="background:linear-gradient(160deg,#a59b8c,#4a4c52)"></div><div class="speaker-name">OSRIC VALE</div></div>
        <div class="speaker"><div class="speaker-photo" role="img" aria-label="Portrait photo of a speaker in a navy suit" style="background:linear-gradient(160deg,#9fb3c6,#1f3558)"></div><div class="speaker-name">DARIO KLEM</div></div>
        <div class="speaker"><div class="speaker-photo" role="img" aria-label="Portrait photo of a speaker in a checked shirt" style="background:linear-gradient(160deg,#a4a4a2,#d9d9dc)"></div><div class="speaker-name">NADIA FORST</div></div>
        <div class="speaker"><div class="speaker-photo" role="img" aria-label="Portrait photo of a speaker in a black blazer" style="background:linear-gradient(160deg,#e6e7ea,#2b2b2e)"></div><div class="speaker-name">MIRA SOLANO</div></div>
      </div>
    </div>
    <div class="copyright" style="top:357px">Copyright © 2020 All Rights Reserved</div>
  </main>
</section>

<!-- Stage screen -->
<section class="screen" style="left:586px;top:31px;height:523px">
  <header class="topbar">
    <div class="brand"><span>EVENTRIX</span><span class="brand-mark"></span></div>
    <div class="duration"><div class="duration-label">EVENT<br>DURATION</div><div class="duration-sep"></div><div class="clock">16:55<small>HH MM</small></div></div>
  </header>
  <nav class="sidenav">
    <div class="nav-item"><svg><use href="#i-cal"/></svg>EVENT INFO</div>
    <div class="nav-item active"><svg><use href="#i-stage"/></svg>STAGE</div>
    <div class="nav-item"><svg><use href="#i-break"/></svg>BREAKOUTS</div>
    <div class="nav-item tall"><svg><use href="#i-expo"/></svg>VIRTUAL<br>EXHIBITION</div>
    <div class="nav-item"><svg><use href="#i-reward"/></svg>REWARDS</div>
  </nav>
  <main class="main">
    <div class="video" role="img" aria-label="Live stage video: presenter at a desk on a phone call with a laptop">
      <div class="play"><svg viewBox="0 0 10 10"><path d="M2 1l7 4-7 4z"/></svg></div>
      <div class="video-caption">LOREM IPSUM DOLOR SIT AMETCONSECTETUR</div>
    </div>
    <aside class="chat">
      <h3>CHAT</h3>
      <div class="chat-list">
        <div class="msg"><div class="avatar" role="img" aria-label="Chat user avatar"></div><div><b>Talia</b><span>Lorem ipsum dolor sit amet consectetur</span></div><time>12:30</time></div>
        <div class="msg"><div class="avatar" role="img" aria-label="Chat user avatar"></div><div><b>Kellan</b><span>Lorem ipsum dolor sit amet consectetur</span></div><time>12:30</time></div>
        <div class="msg"><div class="avatar" role="img" aria-label="Chat user avatar"></div><div><b>Brodie</b><span>Lorem ipsum dolor sit amet consectetur</span></div><time>12:30</time></div>
        <div class="msg"><div class="avatar" role="img" aria-label="Chat user avatar"></div><div><b>Linnea</b><span>Lorem ipsum dolor sit amet consectetur</span></div><time>12:30</time></div>
        <div class="msg"><div class="avatar" role="img" aria-label="Chat user avatar"></div><div><b>Corwin</b><span>Lorem ipsum dolor sit amet consectetur</span></div><time>12:30</time></div>
        <div class="msg"><div class="avatar" role="img" aria-label="Chat user avatar"></div><div><b>Asha</b><span>Lorem ipsum dolor sit amet consectetur</span></div><time>12:30</time></div>
        <div class="msg"><div class="avatar" role="img" aria-label="Chat user avatar"></div><div><b>Jules</b><span>Lorem ipsum dolor sit amet consectetur</span></div><time>12:30</time></div>
      </div>
      <div class="chat-input">Start Typing<svg viewBox="0 0 10 10"><path d="M0 4.5 10 0 6 10 4.8 5.5z"/></svg></div>
    </aside>
    <div class="card agenda" style="left:8px;top:279px;width:436px;height:56px">
      <div class="agenda-icon"><svg><use href="#i-agenda"/></svg></div>
      <div><div class="card-title">AGENDA</div><p>Lorem ipsum dolor sit amet, consectetur adipiscing elit, sed do eiusmod tempor incididunt ut labore et dolore magna aliqua. Ut enim ad minim veniam, quis nostrud exercitation ullamco laboris nisi ut aliquip.</p></div>
    </div>
    <div class="card program" style="left:8px;top:345px;width:436px;height:108px">
      <div class="card-title">PROGRAMMING</div>
      <div class="program-grid">
        <div class="program-item"><h4>LOREM IPSUM DOLOR SIT AMET CONSECTETUR ADIPISCING</h4><p>Lorem ipsum dolor sit amet, consectetur adipiscing elit, sed do eiusmod tempor elit, sed do eiusmod tempor incididunt</p></div>
        <div class="program-item"><h4>LOREM IPSUM DOLOR SIT AMET CONSECTETUR ADIPISCING</h4><p>Lorem ipsum dolor sit amet, consectetur adipiscing elit, sed do eiusmod tempor elit, sed do eiusmod tempor incididunt</p></div>
        <div class="program-item"><h4>LOREM IPSUM DOLOR SIT AMET CONSECTETUR ADIPISCING</h4><p>Lorem ipsum dolor sit amet, consectetur adipiscing elit, sed do eiusmod tempor elit, sed do eiusmod tempor incididunt</p></div>
        <div class="program-item"><h4>LOREM IPSUM DOLOR SIT AMET CONSECTETUR ADIPISCING</h4><p>Lorem ipsum dolor sit amet, consectetur adipiscing elit, sed do eiusmod tempor elit, sed do eiusmod tempor incididunt</p></div>
      </div>
    </div>
    <div class="copyright" style="top:471px">Copyright © 2020 All Rights Reserved</div>
  </main>
</section>

<!-- Breakouts screen -->
<section class="screen" style="left:24px;top:463px;height:330px">
  <header class="topbar">
    <div class="brand"><span>EVENTRIX</span><span class="brand-mark"></span></div>
    <div class="duration"><div class="duration-label">EVENT<br>DURATION</div><div class="duration-sep"></div><div class="clock">16:55<small>HH MM</small></div></div>
  </header>
  <nav class="sidenav">
    <div class="nav-item"><svg><use href="#i-cal"/></svg>EVENT INFO</div>
    <div class="nav-item"><svg><use href="#i-stage"/></svg>STAGE</div>
    <div class="nav-item active"><svg><use href="#i-break"/></svg>BREAKOUTS</div>
    <div class="nav-item tall"><svg><use href="#i-expo"/></svg>VIRTUAL<br>EXHIBITION</div>
    <div class="nav-item"><svg><use href="#i-reward"/></svg>REWARDS</div>
  </nav>
  <main class="main">
    <div class="rooms">
      <div class="room" role="img" aria-label="Conference room photo for breakout room 1"><div class="zoom"><svg><use href="#i-search"/></svg></div><h3>JOIN BREAKOUT ROOM 1</h3><div class="room-time">3.00PM TO 4.30PM</div><div class="room-count">(4/50)</div></div>
      <div class="room" role="img" aria-label="Conference room photo for breakout room 2"><div class="zoom"><svg><use href="#i-search"/></svg></div><h3>JOIN BREAKOUT ROOM 2</h3><div class="room-time">3.00PM TO 4.30PM</div><div class="room-count">(10/50)</div></div>
      <div class="room" role="img" aria-label="Conference room photo for breakout room 3"><div class="zoom"><svg><use href="#i-search"/></svg></div><h3>JOIN BREAKOUT ROOM 3</h3><div class="room-time">3.00PM TO 4.30PM</div><div class="room-count">(4/50)</div></div>
      <div class="room" role="img" aria-label="Conference room photo for breakout room 4"><div class="zoom"><svg><use href="#i-search"/></svg></div><h3>JOIN BREAKOUT ROOM 4</h3><div class="room-time">3.00PM TO 4.30PM</div><div class="room-count">(10/50)</div></div>
    </div>
    <div class="copyright" style="top:277px">Copyright © 2020 All Rights Reserved</div>
  </main>
</section>

<!-- Virtual exhibition screen -->
<section class="screen" style="left:586px;top:575px;height:350px">
  <header class="topbar">
    <div class="brand"><span>EVENTRIX</span><span class="brand-mark"></span></div>
    <div class="duration"><div class="duration-label">EVENT<br>DURATION</div><div class="duration-sep"></div><div class="clock">16:55<small>HH MM</small></div></div>
  </header>
  <nav class="sidenav">
    <div class="nav-item"><svg><use href="#i-cal"/></svg>EVENT INFO</div>
    <div class="nav-item"><svg><use href="#i-stage"/></svg>STAGE</div>
    <div class="nav-item"><svg><use href="#i-break"/></svg>BREAKOUTS</div>
    <div class="nav-item tall active"><svg><use href="#i-expo"/></svg>VIRTUAL<br>EXHIBITION</div>
    <div class="nav-item"><svg><use href="#i-reward"/></svg>REWARDS</div>
  </nav>
  <main class="main">
    <div class="expo" role="img" aria-label="Isometric illustration of a virtual exhibition hall with booths, screens and visitors"></div>
    <div class="expo-actions"><span class="btn">CLICK HERE</span><span class="btn">FIND OUT MORE</span></div>
    <div class="copyright" style="top:295px">Copyright © 2020 All Rights Reserved</div>
  </main>
</section>

<!-- Rewards screen -->
<section class="screen" style="left:24px;top:817px;height:350px">
  <header class="topbar">
    <div class="brand"><span>EVENTRIX</span><span class="brand-mark"></span></div>
    <div class="duration"><div class="duration-label">EVENT<br>DURATION</div><div class="duration-sep"></div><div class="clock">16:55<small>HH MM</small></div></div>
  </header>
  <nav class="sidenav">
    <div class="nav-item"><svg><use href="#i-cal"/></svg>EVENT INFO</div>
    <div class="nav-item"><svg><use href="#i-stage"/></svg>STAGE</div>
    <div class="nav-item"><svg><use href="#i-break"/></svg>BREAKOUTS</div>
    <div class="nav-item tall"><svg><use href="#i-expo"/></svg>VIRTUAL<br>EXHIBITION</div>
    <div class="nav-item active" style="height:55px"><svg><use href="#i-reward"/></svg>REWARDS</div>
  </nav>
  <main class="main">
    <div class="badge" style="left:21px;width:134px"><svg class="tick"><use href="#i-check"/></svg><svg class="ic"><use href="#i-expo"/></svg><p>VISITED VIRTUAL EXHIBITION</p></div>
    <div class="badge" style="left:164px;width:134px"><svg class="tick"><use href="#i-check"/></svg><svg class="ic"><use href="#i-break"/></svg><p>JOINED BREAKOUT ROOM</p></div>
    <div class="badge" style="left:307px;width:133px"><svg class="tick"><use href="#i-check"/></svg><svg class="ic" viewBox="0 0 14 12"><use href="#i-hands"/></svg><p>CHECKED OUT BOOTHS</p></div>
    <div class="points"><strong>40</strong><span>TOTAL POINTS</span></div>
    <div class="reward-title">COLLECT REWARD - TRIGGER EMAIL/LINK TO 3RD PARTY APP</div>
    <div class="reward-note">(Flash them a PROMO CODE/“Email will be given to you on how you can claim your prize)</div>
    <div class="reward-link">they can go to <a href="#">www.prizelane.com</a> to claim</div>
    <div class="copyright" style="top:291px">Copyright © 2020 All Rights Reserved</div>
  </main>
</section>
</body>
</html>
```